Start-up company developing economical and ecological hydrogen peroxide generator needs an attractiv

We need a powerpoint design for a start-up company based in Montreal called Verolune currently seeking to raise funds from investors. We develop an electrochemical hydrogen peroxide generator based on new generation catalysts.

These generators allow industrial users of hydrogen peroxide to generate it onsite economically and ecologically, as opposed to buying it from the major suppliers who make it large production plants using more polluting methods and need to transport it to customers over long distances.

We would like to see designs that have a cleantech technology and green chemistry feel. Colors that evoke a sense of environmental sustainability are desired.

The final design should communicate technological innovation that makes the world a cleaner and healthier place to live.

Target Market(s)

Industrial users or producers of of hydrogen peroxide

Industry/Entity Type

It Company

Font styles to use
Sans Serif

Colors
0255a3
3276b5
85acd3
9bcb3b
add136
e3eebf

Requirements
Must have
• Clean, attractive, professional and advanced technology look.
• Our slogan is: Catalyst for innovation
Nice to have
• The cover page should have our logo and our slogan. It should also have some graphics that pertain to technology and green chemistry. The perception that one should have when looking at it is that the company is developing a clean chemical manufacturing technology that is more environmentally friendly.
• Each other template page should have our logo discretely included in it.
• Other than the cover page, the template pages should not be too crowded with design elements. There should be lots of clear space to add material.
• I have uploaded some inspirational images that can be used to help come up with some designs.

```html
<!DOCTYPE html>
<html lang="en">
<head>
<meta charset="utf-8">
<title>Verolune – Presentation Template</title>
<link href="https://fonts.googleapis.com/css2?family=Lato:ital,wght@0,300;0,400;0,700;1,400&display=swap" rel="stylesheet">
<style>
  :root{
    --stage:#a7b0b6;
    --paper:#ffffff;
    --header-band:#eef1f6;
    --title-grey:#8c95a8;
    --text:#4a4f5a;
    --footer-blue:#2a75b8;
    --navy:#163f82;
    --blue:#2a75b8;
    --sky:#85acd3;
    --lime:#add136;
    --grid:#3a5aa8;
    --axis:#7a8fbf;
  }
  *{box-sizing:border-box;margin:0;padding:0}
  html,body{width:1200px;height:910px;overflow:hidden;background:var(--stage);font-family:'Lato',Arial,sans-serif}
  .slide{position:absolute;width:582px;height:436px;background:var(--paper);overflow:hidden}
  .slide--bullets{left:14px;top:12px}
  .slide--graphs{left:606px;top:12px}
  .slide--closing{left:14px;top:459px;height:435px}

  .slide__header{position:absolute;left:0;top:0;width:100%;height:55px;background:var(--header-band);border-bottom:1px solid #e1e5ee;text-align:center}
  .slide__title{font-weight:400;font-size:27px;letter-spacing:1px;color:var(--title-grey);line-height:1;padding-top:14px}
  .slide__subtitle{font-size:9.5px;color:var(--title-grey);letter-spacing:.4px;margin-top:1px}
  .slide__subtitle b{font-weight:700}

  .slide__footer{position:absolute;left:0;bottom:0;width:100%;height:35px;background:var(--footer-blue);color:#fff;display:flex;align-items:center;font-size:11px}
  .footer__brand{font-size:13px;font-weight:400;width:86px;padding-left:13px}
  .footer__slogan b{font-weight:700}
  .footer__page{margin-left:auto;padding-right:20px;font-weight:700;font-size:10px}

  .bullets{list-style:none;position:absolute;color:var(--text)}
  .bullets li{position:relative}
  .bullets li::before{content:"";position:absolute;left:-16px;top:3px;border-left:4px solid var(--blue);border-top:3px solid transparent;border-bottom:3px solid transparent}
  .bullets b{font-weight:700}
  .bullets--main{left:78px;top:123px;width:450px;font-size:10px;line-height:12.6px}
  .bullets--main li{margin-bottom:12.5px}
  .bullets--small{top:311px;width:210px;font-size:7.4px;line-height:10px}
  .bullets--small li{margin-bottom:10px}
  .bullets--small li::before{left:-13px;top:2px;border-left-width:3px;border-top-width:2.5px;border-bottom-width:2.5px}

  .graph-title{position:absolute;top:80px;font-size:16.5px;color:var(--text);font-weight:400}
  .graph-title b{font-weight:700}
  .graph-svg{position:absolute;left:0;top:0}

  .closing__backdrop{position:absolute;inset:0;background:linear-gradient(180deg,#fbfcfe 0%,#eef1f6 55%,#dfe4ec 100%)}
  .closing__brand{position:absolute;left:0;width:100%;top:62px;text-align:center;font-size:72px;font-weight:400;color:#8c93a6;letter-spacing:1px}
  .closing__rule{position:absolute;left:208px;width:165px;height:1px;background:#6c7590}
  .contact{position:absolute;left:190px;width:200px;top:251px;text-align:center;color:#8a91a2;font-size:12px;line-height:14.5px}
  .contact dt{font-weight:700}
  .contact dd{font-style:italic}
  .contact dd.plain{font-style:normal}
  .contact .gap{margin-top:13px}
  .social{position:absolute;right:22px;bottom:14px;display:flex;gap:9px}
  .social span{width:13px;height:13px;border-radius:50%;background:#8a91a2}
</style>
</head>
<body>

<section class="slide slide--bullets">
  <header class="slide__header">
    <h1 class="slide__title">JUST TEXT WITH BULLETS</h1>
    <p class="slide__subtitle">YOU CAN CUSTOMIZE YOUR BULLETS</p>
  </header>
  <ul class="bullets bullets--main">
    <li><b>Aenean</b> ridiculus tortor quis interdum id habitant ad, natoque consectetuer nisl auctor libero quisque euismod ante inceptos malesuada ligula mattis.</li>
    <li><b>Aenean</b> ridiculus tortor quis interdum id habitant ad, natoque consectetuer nisl auctor libero quisque euismod ante inceptos malesuada ligula mattis.</li>
    <li>Nulla, netus pulvinar pellentesque porttitor purus maecenas tellus hac nulla lacus. Lorem. Nostra laoreet nulla, dis cursus nascetur dolor odio Eu Magna molestie montes dui mus cursus habitasse mauris tempor.</li>
    <li>Varius inceptos <b>nascetur</b> mollis dui aptent ultrices. Pretium pulvinar ante lobortis convallis lectus netus vitae penatibus eros at blandit. Parturient.</li>
    <li>Varius inceptos <b>nascetur</b> mollis dui aptent ultrices. Pretium pulvinar ante lobortis convallis lectus netus vitae penatibus eros at blandit. Parturient.</li>
  </ul>
  <footer class="slide__footer">
    <span class="footer__brand">Verolune</span>
    <span class="footer__slogan">Catalyst for innovation | <b>PRESENTATION NAME</b></span>
    <span class="footer__page">7</span>
  </footer>
</section>

<section class="slide slide--graphs">
  <header class="slide__header">
    <h1 class="slide__title">COLOR STYLE GRAPHS</h1>
    <p class="slide__subtitle">CHOOSE TO USE BETWEEN <b>MAIN</b> AND <b>SECONDARY</b> COLOR THEMES</p>
  </header>

  <h2 class="graph-title" style="left:29px"><b>Graph</b> Main Colors</h2>
  <h2 class="graph-title" style="left:331px"><b>Graph</b> Secondary Colors</h2>

  <svg class="graph-svg" width="582" height="300" viewBox="0 0 582 300" font-family="Lato, Arial, sans-serif">
    <!-- area chart -->
    <g class="area-chart">
      <polygon fill="var(--navy)" points="52,286 52,196 122,215 192,171 262,181 262,286"/>
      <polygon fill="var(--sky)" points="52,286 52,237 122,255 262,255 262,286"/>
      <g stroke="var(--grid)" stroke-width="1">
        <line x1="52" y1="122" x2="262" y2="122"/>
        <line x1="52" y1="163" x2="262" y2="163"/>
        <line x1="52" y1="204" x2="215" y2="204"/>
        <line x1="52" y1="245" x2="262" y2="245"/>
      </g>
      <polygon fill="var(--lime)" points="52,286 52,258 122,243 192,196 262,129 262,286"/>
      <g fill="var(--axis)" font-size="7.5" text-anchor="end">
        <text x="44" y="125">100</text><text x="44" y="166">75</text>
        <text x="44" y="207">50</text><text x="44" y="248">25</text><text x="44" y="289">0</text>
      </g>
      <g fill="#555" font-size="7.5" text-anchor="middle">
        <text x="52" y="297">2007</text><text x="122" y="297">2008</text>
        <text x="192" y="297">2009</text><text x="262" y="297">2010</text>
      </g>
    </g>
    <!-- pie chart -->
    <g class="pie-chart">
      <path fill="var(--navy)" d="M419 198 L366.4 277.1 A95 95 0 0 1 466.5 115.7 Z"/>
      <path fill="var(--blue)" d="M419 198 L506.6 234.8 A95 95 0 0 1 366.4 277.1 Z"/>
      <path fill="var(--sky)" d="M419 198 L503.2 154 A95 95 0 0 1 506.6 234.8 Z"/>
      <path fill="var(--lime)" stroke="#fff" stroke-width="2" transform="translate(7,-7)" d="M419 198 L466.5 115.7 A95 95 0 0 1 503.2 154 Z"/>
      <g fill="#fff" font-size="10.5" text-anchor="middle">
        <text x="378" y="182">50%</text><text x="439" y="266">28%</text>
        <text x="483" y="204">14%</text><text x="476" y="154">9%</text>
      </g>
      <g font-size="6.5" fill="#333">
        <circle cx="502" cy="267" r="3" fill="var(--lime)"/><text x="508" y="269.5">2007</text>
        <circle cx="533" cy="267" r="3" fill="var(--sky)"/><text x="539" y="269.5">2008</text>
        <circle cx="502" cy="277" r="3" fill="var(--blue)"/><text x="508" y="279.5">2009</text>
        <circle cx="533" cy="277" r="3" fill="var(--navy)"/><text x="539" y="279.5">2010</text>
      </g>
    </g>
  </svg>

  <ul class="bullets bullets--small" style="left:54px">
    <li><b>Aenean</b> ridiculus tortor quis interdum id habitant ad, natoque consectetuer nisl auctor libero quisque euismod ante inceptos malesuada ligula mattis.</li>
    <li>Varius inceptos <b>nascetur</b> mollis dui aptent ultrices. Pretium pulvinar ante lobortis convallis lectus netus vitae penatibus eros at blandit. Parturient.</li>
  </ul>
  <ul class="bullets bullets--small" style="left:339px">
    <li><b>Aenean</b> ridiculus tortor quis interdum id habitant ad, natoque consectetuer nisl auctor libero quisque euismod ante inceptos malesuada ligula mattis.</li>
    <li>Varius inceptos <b>nascetur</b> mollis dui aptent ultrices. Pretium pulvinar ante lobortis convallis lectus netus vitae penatibus eros at blandit. Parturient.</li>
  </ul>

  <footer class="slide__footer">
    <span class="footer__brand">Verolune</span>
    <span class="footer__slogan">Catalyst for innovation | <b>PRESENTATION NAME</b></span>
    <span class="footer__page">8</span>
  </footer>
</section>

<section class="slide slide--closing">
  <div class="closing__backdrop" role="img" aria-label="Soft light background with a faint hexagon molecular pattern"></div>
  <div class="closing__brand">Verolune</div>
  <div class="closing__rule" style="top:240px"></div>
  <dl class="contact">
    <dt>Contact us:</dt>
    <dd class="plain">888-888-8888</dd>
    <dd>info@verolune.com</dd>
    <dt class="gap">Central Office:</dt>
    <dd>Address Line 1</dd>
    <dd>Address Line 2</dd>
  </dl>
  <div class="closing__rule" style="top:364px"></div>
  <div class="social" aria-label="Social links"><span></span><span></span><span></span><span></span></div>
</section>

</body>
</html>
```